Book cover design for modern bagpipe music book

This music book will be A4 in size and requires a design for the front and back cover. The focus is on creating a modern and eye catching design, breaking away from the stereotypes of what people think of when they think of bagpipes. Think the OPPOSITE of a bagpiper in a full kilt standing on top of a mountain playing Lanterns on the Moor!

Book title: Wake Stroll Hum Again

Other front cover text : Music for the bagpipes by Dara Colby

Front cover file ideas uploaded

2 pictures of bagpipes attached.

- The real set of bagpipes give an idea of the correct finer details

- The toy bagpipes perhaps have a better shape with the left 'stick' down

Back cover - No real brief. Keen for it not to be a full block single colour though.

Design requires 3mm bleed for print

Open to ideas and suggestions! Thank you!

```html
<!DOCTYPE html>
<html lang="en">
<head>
<meta charset="utf-8">
<title>Wake Stroll Hum Again – Book Cover</title>
<link href="https://fonts.googleapis.com/css2?family=Barlow+Condensed:wght@500;600&display=swap" rel="stylesheet">
<style>
  :root {
    --backdrop: #d3d3d3;
    --navy: #022334;
    --orange: #d98a1f;
    --red: #c41e24;
    --teal: #5f9189;
    --green: #8ab534;
    --chalk: #efefeb;
    --pipe-black: #0b0b0b;
    --tartan-red: #b91c22;
  }
  * { margin: 0; padding: 0; box-sizing: border-box; }
  html, body {
    width: 1183px; height: 1200px; overflow: hidden;
    background: var(--backdrop);
  }
  .cover {
    position: absolute; left: 187px; top: 0;
    width: 808px; height: 1200px;
    background: var(--navy);
    overflow: hidden;
    font-family: "Barlow Condensed", "Arial Narrow", sans-serif;
  }
  .pipes-art {
    position: absolute; left: 640px; top: 48px;
    width: 168px; height: 1045px;
    background: linear-gradient(180deg, #0e1a22 0%, #141414 55%, var(--tartan-red) 100%);
  }
  .title-line {
    position: absolute; left: 68px;
    height: 160px;
    display: flex; align-items: stretch;
    font-weight: 500;
    font-size: 222px;
    line-height: 160px;
    letter-spacing: -4px;
  }
  .title-line .word { display: block; height: 160px; line-height: 182px; position: relative; z-index: 2; }
  .title-line .last { color: var(--chalk); }
  .icon-box {
    position: relative; z-index: 1;
    height: 160px;
    margin-left: -34px;
    border-radius: 0 12px 12px 0;
    display: flex; align-items: center; justify-content: flex-end;
    padding-right: 22px;
  }
  .icon-box svg, .icon-box .icon-art { width: 120px; height: 120px; }
  .line-wake  { top: 142px; color: var(--orange); }
  .line-wake .icon-box  { background: var(--orange); width: 215px; }
  .line-stroll { top: 344px; color: var(--red); }
  .line-stroll .icon-box { background: var(--red); width: 205px; }
  .line-hum   { top: 545px; color: var(--teal); }
  .line-hum .icon-box   { background: var(--teal); width: 215px; }
  .line-again { top: 748px; color: var(--green); }
  .line-again .icon-box { background: var(--green); width: 205px; }
  .icon-art { border-radius: 6px; background: #1f4a50; }
  .subtitle {
    position: absolute; left: 76px; top: 978px;
    color: var(--orange);
    font-size: 44px; font-weight: 500; letter-spacing: -0.5px;
  }
  .author-band {
    position: absolute; left: 0; top: 1031px;
    width: 410px; height: 68px;
    background: var(--orange);
    color: var(--navy);
    font-size: 58px; font-weight: 500;
    line-height: 70px;
    padding-left: 76px;
    letter-spacing: -1px;
    white-space: nowrap;
  }
</style>
</head>
<body>
<main class="cover">
  <div class="pipes-art" role="img" aria-label="Illustration of black bagpipe drones with red cords over a red tartan bag"></div>

  <h1 class="title">
    <span class="title-line line-wake">
      <span class="word">WAK<span class="last">E</span></span>
      <span class="icon-box">
        <svg viewBox="0 0 100 100" aria-label="knife and fork icon">
          <g fill="var(--navy)">
            <path d="M14 10 C30 18 52 40 60 58 L52 64 C38 48 20 30 14 10Z"/>
            <rect x="54" y="56" width="12" height="40" rx="6" transform="rotate(-45 60 76)"/>
            <path d="M62 8 l5 0 0 18 4 0 0-18 5 0 0 18 4 0 0-18 5 0 0 22 c0 8-6 12-12 12 L40 88 c-3 3-8 3-10 0 c-2-3-1-6 2-8 L66 44 c-4-4-4-10-4-14Z" transform="rotate(0)"/>
          </g>
        </svg>
      </span>
    </span>

    <span class="title-line line-stroll">
      <span class="word">STROL<span class="last">L</span></span>
      <span class="icon-box">
        <svg viewBox="0 0 100 100" aria-label="bed icon">
          <g fill="none" stroke="var(--chalk)" stroke-width="6">
            <path d="M8 30 V82 M8 64 H92 M92 50 V82 M34 50 H92"/>
          </g>
          <circle cx="22" cy="46" r="8" fill="var(--chalk)"/>
        </svg>
      </span>
    </span>

    <span class="title-line line-hum">
      <span class="word">HU<span class="last">M</span></span>
      <span class="icon-box">
        <span class="icon-art" role="img" aria-label="Small bagpipe pictogram"></span>
      </span>
    </span>

    <span class="title-line line-again">
      <span class="word">AGAI<span class="last">N</span></span>
      <span class="icon-box">
        <svg viewBox="0 0 100 100" aria-label="repeat arrows icon">
          <g fill="none" stroke="var(--navy)" stroke-width="10" stroke-linejoin="round">
            <path d="M18 60 V22 H66"/>
            <path d="M82 40 V78 H34"/>
          </g>
          <path d="M62 6 L86 22 L62 38Z" fill="var(--navy)"/>
          <path d="M38 62 L14 78 L38 94Z" fill="var(--navy)"/>
        </svg>
      </span>
    </span>
  </h1>

  <p class="subtitle">Music for the bagpipes</p>
  <p class="author-band">BY DARA COLBY</p>
</main>
</body>
</html>
```